Design Tweak needed for a current site

Design on top of an existing quiz funnel

Ideally we would like to tweak what we have already built here (moving elements, styles, adding simple elements etc): http://offers.plumrivetdeals.com/can-you-save-on-car-insurance

The flow:
1) User lands on the quiz page
2) User answers X questions and moves through the flow
3) Calculating user results screen
4) User reaches a success screen, and is subsequently redirected

Keys to the design:
1) We need to emphasize the quiz title as that will drive engagement. In this case, this is a quiz to see if you might be eligible to save money on car insurance.

2) At the end of the quiz we need to make it very, very clear that the user is eligible for savings and that in order to complete the process they are being redirected to another page where they need to fill out a form. It is critical that the design communicates this very clearly... We can count down the time left until redirect and we can use any order of elements to make this point. I think our current design does a very bad job of this.

3) We want to have a "calculating" step so that it seems like the page is working in the background

Goals of the design:
1) Polished, high quality experience throughout
2) User is clearly prepared to be redirected to the conversion funnel/landing page at the end
3) User understands the value of completing the quiz

Target Market(s)

designers

Industry/Entity Type

Moving

Number of Pages Required

1 page

Font styles to use
Sans Serif

Colors

Designer to choose colors to be used in the design.

Requirements
Must have
• This quiz funnel is a template so while the current use case is for auto insurance, we would like a design that also would work in other contexts.
Should not have
• We don't want to materially change the core functionality of the quiz itself... redesigning any of the elements or interactions is encouraged though

```html
<!DOCTYPE html>
<html lang="en">
<head>
<meta charset="utf-8">
<title>PlumRivetDeals – Quiz</title>
<link rel="stylesheet" href="https://fonts.googleapis.com/css2?family=Montserrat:wght@500;700;800&family=Outfit:wght@400;500&display=swap">
<style>
  :root {
    --green-dark: #52ac4c;
    --green-light: #6cc767;
    --green-bar: #55ad4f;
    --ring: #3db878;
    --tick: #3db878;
    --indigo: #4450a5;
    --white: #ffffff;
    --ink: #111111;
  }
  * { margin: 0; padding: 0; box-sizing: border-box; }
  html, body { width: 1200px; height: 675px; overflow: hidden; background: var(--white); }
  .stage { position: relative; width: 1200px; height: 675px; overflow: hidden; font-family: "Montserrat", sans-serif; }

  .site-header {
    position: absolute; left: 0; top: 0; width: 1200px; height: 104px;
    background: radial-gradient(ellipse 420px 180px at 820px 40px, var(--green-light), var(--green-dark) 100%);
  }
  .brand { position: absolute; left: 34px; top: 20px; display: flex; align-items: center; gap: 15px; }
  .brand-dot { width: 61px; height: 61px; border-radius: 50%; background: var(--white); }
  .brand-name { font-family: "Outfit", sans-serif; font-weight: 500; font-size: 50px; color: var(--white); letter-spacing: 0.2px; }

  .question {
    position: absolute; left: 0; top: 182px; width: 1200px; text-align: center;
    font-weight: 800; font-size: 35px; line-height: 43px; letter-spacing: 2px; color: var(--indigo);
  }

  .answer {
    position: absolute; top: 299px; width: 174px; height: 166px;
    border: 3px solid var(--ring); border-radius: 50%;
    display: flex; flex-direction: column; align-items: center; justify-content: center;
  }
  .answer-yes { left: 416px; }
  .answer-no { left: 629px; }
  .answer svg { width: 60px; height: 60px; margin-top: -6px; }
  .answer-label { font-family: "Outfit", sans-serif; font-weight: 500; font-size: 29px; color: var(--indigo); letter-spacing: 1.5px; margin-top: 4px; }

  .progress { position: absolute; left: 502px; top: 548px; width: 220px; }
  .progress-step { font-size: 15px; font-weight: 500; color: var(--ink); letter-spacing: 0.6px; }
  .progress-bar { display: flex; margin-top: 10px; height: 16px; }
  .progress-seg { flex: 1; background: var(--green-bar); border-radius: 8px; border: 1.5px solid var(--white); margin-left: -8px; }
  .progress-seg:first-child { margin-left: 0; }
  .progress-done { font-size: 15px; font-weight: 500; color: var(--ink); letter-spacing: 0.6px; text-align: right; margin-top: 7px; padding-right: 8px; }
</style>
</head>
<body>
<main class="stage">
  <header class="site-header">
    <div class="brand">
      <span class="brand-dot"></span>
      <span class="brand-name">PlumRivetDeals</span>
    </div>
  </header>

  <h1 class="question">Have you been in an accident<br>in the last 12 months?</h1>

  <button class="answer answer-yes" type="button" aria-label="Yes">
    <svg viewBox="0 0 60 60" aria-hidden="true">
      <path d="M6 33 L22 48 L54 14" fill="none" stroke="var(--tick)" stroke-width="12" stroke-linecap="round" stroke-linejoin="round"/>
    </svg>
    <span class="answer-label">yes</span>
  </button>

  <button class="answer answer-no" type="button" aria-label="No">
    <svg viewBox="0 0 60 60" aria-hidden="true">
      <path d="M10 10 L50 50 M50 10 L10 50" fill="none" stroke="var(--indigo)" stroke-width="13" stroke-linecap="round"/>
    </svg>
    <span class="answer-label">no</span>
  </button>

  <section class="progress">
    <p class="progress-step">Question 4 to 4</p>
    <div class="progress-bar">
      <span class="progress-seg"></span>
      <span class="progress-seg"></span>
      <span class="progress-seg"></span>
      <span class="progress-seg"></span>
    </div>
    <p class="progress-done">75% completed</p>
  </section>
</main>
</body>
</html>
```